Brookvale Harbour Clinic advertising

I have a copy that we had done several years ago. I loved it and still do. Unfortunately, the original graphic designer lost the original artwork. What I do have is the same artwork at a small fridge magnet size. I need to new artwork to look like the small magnet version.
The main brief is to appeal to our clients who have addiction problems. It needs to be edgy and as far removed from the typical medical center images

Requirements
Must have
• The print quality must be able to be blown up to 1m x 2m.

```html
<!DOCTYPE html>
<html lang="en">
<head>
<meta charset="UTF-8">
<title>Brookvale Harbour Clinic – Heroin Treatment Advertisement</title>
<link rel="stylesheet" href="https://fonts.googleapis.com/css2?family=Montserrat:wght@700;800&family=Open+Sans:wght@700&display=swap">
<style>
  :root {
    --paper: #ffffff;
    --ink: #000000;
    --teal: #2bb298;
    --white: #ffffff;
    --skin-light: #e8c9a8;
    --skin-mid: #b98b68;
    --skin-dark: #4a3020;
  }
  * { margin: 0; padding: 0; box-sizing: border-box; }
  html, body {
    width: 1200px;
    height: 821px;
    overflow: hidden;
    background: var(--paper);
  }
  .canvas {
    position: relative;
    width: 1200px;
    height: 821px;
    background: var(--paper);
  }
  .ad-panel {
    position: absolute;
    left: 45px;
    top: 133px;
    width: 1109px;
    height: 555px;
    background: var(--ink);
    overflow: hidden;
  }
  .headline-tag {
    position: absolute;
    left: 46px;
    top: 75px;
    width: 452px;
    height: 100px;
  }
  .headline-tag svg { position: absolute; inset: 0; }
  .headline-word {
    position: absolute;
    left: 25px;
    top: 0;
    height: 100px;
    line-height: 100px;
    font-family: "Montserrat", sans-serif;
    font-weight: 800;
    font-size: 80px;
    letter-spacing: 0.13em;
    color: var(--white);
  }
  .tagline {
    position: absolute;
    left: 74px;
    top: 195px;
    font-family: "Open Sans", sans-serif;
    font-weight: 700;
    font-size: 39px;
    line-height: 39px;
    color: var(--white);
    letter-spacing: 0.01em;
  }
  .divider-rule {
    position: absolute;
    left: 73px;
    top: 364px;
    width: 515px;
    height: 3px;
    background: var(--teal);
  }
  .clinic-name {
    position: absolute;
    left: 72px;
    top: 377px;
    font-family: "Montserrat", sans-serif;
    font-weight: 800;
    font-size: 30px;
    color: var(--teal);
    white-space: nowrap;
  }
  .offer {
    position: absolute;
    left: 72px;
    top: 419px;
    font-family: "Montserrat", sans-serif;
    font-weight: 700;
    font-size: 29px;
    color: var(--white);
    white-space: nowrap;
  }
  .contact-line {
    position: absolute;
    left: 73px;
    top: 462px;
    height: 44px;
    display: flex;
    align-items: center;
    font-family: "Montserrat", sans-serif;
    font-weight: 800;
    font-size: 29px;
    color: var(--teal);
    white-space: nowrap;
  }
  .contact-phone { font-style: italic; }
  .contact-separator {
    width: 3px;
    height: 44px;
    background: var(--teal);
    margin: 0 14px 0 14px;
  }
  .portrait {
    position: absolute;
    left: 682px;
    top: 0;
            width: 414px;
    height: 517px;
    border-radius: 50% 50% 46% 46% / 44% 44% 56% 56%;
    background: radial-gradient(ellipse at 50% 45%, var(--skin-light) 0%, var(--skin-mid) 55%, var(--skin-dark) 85%, var(--ink) 100%);
  }
</style>
</head>
<body>
<div class="canvas">
  <section class="ad-panel">
    <div class="headline-tag">
      <svg width="452" height="100" viewBox="0 0 452 100" aria-hidden="true">
        <polygon fill="var(--teal)" points="9,0 434,0 434,16 443,27 434,38 443,51 434,62 443,67 434,74 443,79 434,85 434,100 9,100 9,94 4,88 9,82 9,70 4,60 9,53 0,44 9,34 4,27 9,18"/>
      </svg>
      <div class="headline-word">HEROIN</div>
    </div>
    <p class="tagline">Got a Problem?<br>We Can Help.</p>
    <div class="divider-rule"></div>
    <p class="clinic-name">Brookvale Harbour Clinic</p>
    <p class="offer">Free Treatment Available</p>
    <p class="contact-line">
      <span class="contact-phone">9700 41888</span>
      <span class="contact-separator"></span>
      <span class="contact-web">www.brookvaleharbour.com.au</span>
    </p>
    <div class="portrait" role="img" aria-label="Sepia close-up portrait of a young person whose skin is overlaid with dry cracked-earth texture"></div>
  </section>
</div>
</body>
</html>
```